Support People to improve their image and well-being by provided personalised advise

We need a design for business cards that could be used for production on plato press. We build a new business in our region for advising mostly women (also men though) on style embracing several aspects including fashion, style, self-confidence and ultimately your internal and external image. The business card should be "classy", "french-style". The business is located in the french -speaking part of Switzerland, close to France. The name of the company is Velo Grace

Target Market(s)

Service fees won't be cheap (medium to premium) thus we target mid-class to upper-class women (1st target) and men (2nd target)

Industry/Entity Type

Life Coaching

Contact Information for Business Card

Conseil en Image

+41 79 418 62 07
morinetu@velo-grace.ch
linkedin.com/in/tu-moro-netia

Logo Text

Velo Grace

Colors

Designer to choose colors to be used in the design.

```html
<!DOCTYPE html>
<html lang="fr">
<head>
<meta charset="utf-8">
<title>Velo Grace – Business Card</title>
<link rel="stylesheet" href="https://fonts.googleapis.com/css2?family=Great+Vibes&family=Open+Sans:wght@300;700&display=swap">
<style>
  :root {
    --canvas-bg: #ece9e4;
    --card-black: #1f1f20;
    --card-white: #ffffff;
    --gold: #c9971f;
    --ink: #1a1a1a;
    --logo-grey: #b5b5b5;
    --shadow: rgba(0, 0, 0, 0.18);
  }
  * { margin: 0; padding: 0; box-sizing: border-box; }
  html, body {
    width: 1200px;
    height: 842px;
    overflow: hidden;
    background: var(--canvas-bg);
    font-family: "Open Sans", Arial, sans-serif;
  }
  .sheet {
    position: relative;
    width: 1200px;
    height: 842px;
  }
  .card {
    position: absolute;
    top: 272px;
    width: 520px;
    height: 297px;
    box-shadow: 0 10px 28px var(--shadow);
  }
  .card--front {
    left: 60px;
    background: linear-gradient(160deg, #2a2a2b 0%, var(--card-black) 60%, #161617 100%);
    display: flex;
    align-items: center;
    justify-content: center;
  }
  .card--back {
    left: 620px;
    background: var(--card-white);
  }
  .brand {
    font-family: "Open Sans", Arial, sans-serif;
    font-weight: 300;
    letter-spacing: 2px;
    white-space: nowrap;
  }
  .brand--front {
    font-size: 44px;
    color: var(--gold);
  }
  .brand--back {
    position: absolute;
    left: 30px;
    top: 206px;
    font-size: 30px;
    color: var(--logo-grey);
  }
  .tagline {
    position: absolute;
    left: 232px;
    top: 26px;
    font-family: "Great Vibes", cursive;
    font-size: 40px;
    color: var(--gold);
    white-space: nowrap;
  }
  .identity {
    position: absolute;
    right: 262px;
    top: 112px;
    text-align: right;
    color: var(--ink);
  }
  .identity__name {
    font-weight: 700;
    font-size: 17px;
  }
  .identity__role {
    font-weight: 700;
    font-size: 11px;
    margin-top: 2px;
  }
  .divider {
    position: absolute;
    left: 272px;
    top: 110px;
    width: 2px;
    height: 96px;
    background: var(--ink);
  }
  .contact {
    position: absolute;
    left: 288px;
    top: 146px;
    list-style: none;
    color: var(--ink);
    font-weight: 700;
    font-size: 13.5px;
    line-height: 22px;
  }
  .contact__item {
    display: flex;
    align-items: center;
    gap: 7px;
    white-space: nowrap;
  }
  .contact__icon {
    width: 12px;
    height: 12px;
    flex: none;
    fill: var(--ink);
  }
</style>
</head>
<body>
<main class="sheet">
  <section class="card card--front" aria-label="Card front">
    <span class="brand brand--front">Velo Grace</span>
  </section>

  <section class="card card--back" aria-label="Card back">
    <p class="tagline">Conseil en Image</p>

    <div class="identity">
      <p class="identity__name">Tu Moro Netia</p>
      <p class="identity__role">Owner</p>
    </div>

    <span class="divider" aria-hidden="true"></span>

    <ul class="contact">
      <li class="contact__item">
        <svg class="contact__icon" viewBox="0 0 24 24" aria-hidden="true">
          <path d="M6.6 10.8a15.1 15.1 0 0 0 6.6 6.6l2.2-2.2a1 1 0 0 1 1-.25 11.4 11.4 0 0 0 3.6.57 1 1 0 0 1 1 1V20a1 1 0 0 1-1 1A17 17 0 0 1 3 4a1 1 0 0 1 1-1h3.5a1 1 0 0 1 1 1c0 1.25.2 2.45.57 3.57a1 1 0 0 1-.25 1z"/>
        </svg>
        <span>+41 79 418 62 07</span>
      </li>
      <li class="contact__item">
        <svg class="contact__icon" viewBox="0 0 24 24" aria-hidden="true">
          <path d="M2 5h20v14H2z M2 5l10 8 10-8" fill="none" stroke="#1a1a1a" stroke-width="2.4"/>
        </svg>
        <span>morinetu@velo-grace.ch</span>
      </li>
      <li class="contact__item">
        <svg class="contact__icon" viewBox="0 0 24 24" aria-hidden="true">
          <rect x="2" y="2" width="20" height="20" rx="3"/>
        </svg>
        <span>Tu Moro Netia</span>
      </li>
    </ul>

    <span class="brand brand--back">Velo Grace</span>
  </section>
</main>
</body>
</html>
```